Industry automation wholesale website

www.velqora.eu provides solutions for automation, building automation and digital signage.

Our products are rugged, reliable, energy saving and representative.

Scope of pages:
● welcome page
- scope of products
- applications, success stories and news
● category page
- short introduction
- sub categories
- product highlights
● product page
- short introduction
- about 3 to 4 pictures
- technical specifications: materials, dimensions
- price
- related products

Optional:
● contact page
- address
- contact form
● blog
- picture
- text
● logo
● favicon / apple touch icon

Conclusion:
● We need a professionally looking site
● Bright colors (e.g. white, grey, metalic colors, blue)

some pages we like:
http://www.brundafel.de/
http://www.korvimash.de/

Target Market(s)

Our target market is the industrial sector
● Target audience: engineering and IT professionals

Industry/Entity Type

Building

Requirements
Must have
• ● only use free available fonts e.g. Pellor Type Library (http://www.pellortype.com/webfonts)
Should not have
• ● sound
● flash

```html
<!DOCTYPE html>
<html lang="en">
<head>
<meta charset="utf-8">
<title>Velqora – Touch Panel PC</title>
<link href="https://fonts.googleapis.com/css2?family=Arimo:wght@400;700&family=Raleway:wght@400;500;600&family=Lato:wght@400;700&family=Open+Sans:wght@700&display=swap" rel="stylesheet">
<style>
:root{
  --blue:#1b6b93;
  --teal-top:#74bfd6;
  --teal-bottom:#3d92ad;
  --page-bg:#e6e6e6;
  --stripe:#dcdcdc;
  --white:#ffffff;
  --text-dark:#444444;
  --text-mid:#555555;
  --footer:#1e1e1e;
  --footer-bottom:#111111;
  --footer-text:#c8c8c8;
  --footer-muted:#7c7c7c;
  --band:#eeeeee;
}
*{box-sizing:border-box;margin:0;padding:0}
html,body{width:1200px;height:1008px;overflow:hidden}
body{position:relative;background:repeating-linear-gradient(135deg,var(--page-bg) 0 3px,var(--stripe) 3px 5px);font-family:'Arimo',Arial,sans-serif;color:var(--text-dark)}
.abs{position:absolute}

.topbar{left:0;top:0;width:1200px;height:33px;background:var(--blue)}
.contact{top:8px;color:var(--white);font-size:14px;display:flex;align-items:center;gap:10px}
.header{left:0;top:33px;width:1200px;height:92px;background:linear-gradient(#ffffff,#f1f1f1);border-bottom:1px solid #e2e2e2}
.brand{left:108px;top:44px;font-family:'Arimo',Arial,sans-serif;font-weight:700;font-size:36px;color:var(--text-dark);letter-spacing:2px;display:flex;align-items:center;gap:12px}
.brand-mark{width:16px;height:16px;background:var(--blue)}
.search{left:870px;top:45px;width:211px;height:26px;border:1px solid #d8d8d8;border-radius:3px;background:var(--white);font-size:11px;color:#999;padding:6px 8px}
.nav a{position:absolute;top:82px;height:31px;line-height:31px;font-size:13px;font-weight:700;color:var(--text-mid);text-decoration:none;text-align:center}
.nav a.active{background:var(--blue);color:var(--white);border-radius:3px}

.page{left:100px;top:125px;width:1000px;height:655px;background:var(--white)}
.hero{left:100px;top:125px;width:1000px;height:378px;background:linear-gradient(90deg,#f6f6f6,#eeeeee)}
.hero-photo{left:416px;top:125px;width:683px;height:363px;background:linear-gradient(135deg,#e8e9ec 0%,#c8ccd3 25%,#3a4a6a 55%,#1b1f2b 78%,#6b3b34 100%)}
.hero-title{left:143px;top:168px;font-size:46px;line-height:48px;font-weight:400;color:var(--text-dark)}
.hero-text{left:145px;top:281px;width:345px;font-size:15px;line-height:22px;color:var(--text-mid)}
.btn-start{left:145px;top:347px;width:161px;height:47px;border-radius:3px;background:linear-gradient(#6a6a6a,#3e3e3e);color:var(--white);font-family:'Raleway',sans-serif;font-weight:600;font-size:16px;line-height:47px;text-align:center}

.features{left:130px;top:488px;width:932px;height:280px;background:var(--white);border:1px solid #dedede;border-bottom:none}
.features-top{left:131px;top:489px;width:930px;height:60px;background:linear-gradient(#e9e9e9,#ffffff)}
.divider{top:510px;width:1px;height:256px;background:#e6e6e6}
.product-img{top:502px;width:160px;height:110px;border-radius:4px}
.band{top:619px;height:38px;background:var(--band)}
.feature-title{top:624px;width:310px;text-align:center;font-family:'Raleway',sans-serif;font-weight:400;font-size:22px;color:var(--text-dark);letter-spacing:.5px}
.feature-text{top:666px;width:260px;text-align:center;font-size:12px;line-height:18px;color:#111}
.btn-learn{top:721px;width:107px;height:28px;border:1px solid #2e7f99;border-radius:2px;background:linear-gradient(var(--teal-top),var(--teal-bottom));font-size:10px;font-weight:700;color:#1c3d4a;text-align:center;line-height:27px}

.footer{left:0;top:780px;width:1200px;height:193px;background:var(--footer)}
.footer-heading{position:absolute;top:793px;font-family:'Open Sans',sans-serif;font-weight:700;font-size:13px;color:var(--white)}
.support{left:111px;top:829px;width:230px;font-family:'Lato',sans-serif;font-size:14.5px;line-height:21px;color:var(--footer-text)}
.support-phone{left:111px;top:905px;font-family:'Lato',sans-serif;font-weight:700;font-size:16px;color:var(--footer-text)}
.post-date{font-family:'Lato',sans-serif;font-size:12px;color:var(--footer-muted)}
.post-title{font-family:'Lato',sans-serif;font-size:14px;line-height:21px;color:#e0e0e0;margin-top:3px}
.tags{left:636px;top:836px;width:210px;display:flex;flex-wrap:wrap;gap:3px}
.tag{border:1px solid #3a3a3a;border-radius:2px;padding:0 10px;height:30px;line-height:30px;font-family:'Lato',sans-serif;font-size:11px;color:#cfcfcf}
.gallery{left:881px;top:836px;width:212px;display:grid;grid-template-columns:repeat(4,50px);gap:4px}
.thumb{width:50px;height:48px;border:1px solid #333;padding:4px;background:#151515}
.thumb span{display:block;width:100%;height:100%}
.legal{left:0;top:973px;width:1200px;height:35px;background:var(--footer-bottom);text-align:center;line-height:38px;font-size:12.5px;color:#666}
.legal span{color:#8a8a8a}
</style>
</head>
<body>

<div class="abs topbar"></div>
<div class="abs contact" style="left:773px">
  <svg width="20" height="16" viewBox="0 0 20 16"><path d="M4 3c2-2 4-2 5 0l-2 2c1 2 2 3 4 4l2-2c2 1 2 3 0 5-3 2-11-5-9-9z" fill="none" stroke="#fff" stroke-width="1.6"/></svg>
  <span>+49-211-5530290</span>
</div>
<div class="abs contact" style="left:943px">
  <svg width="28" height="16" viewBox="0 0 28 16"><rect x="8" y="2" width="18" height="12" fill="none" stroke="#fff" stroke-width="1.5"/><path d="M8 2l9 7 9-7" fill="none" stroke="#fff" stroke-width="1.5"/><path d="M0 5h6M2 9h4M3 12h3" stroke="#fff" stroke-width="1.2"/></svg>
  <span>info@velqora.eu</span>
</div>

<div class="abs header"></div>
<div class="abs brand"><span class="brand-mark"></span><span>VELQORA</span></div>

<div class="abs search">Search here...
  <svg class="abs" style="right:6px;top:6px" width="13" height="13" viewBox="0 0 13 13"><circle cx="5" cy="5" r="4" fill="none" stroke="#999" stroke-width="2"/><path d="M8 8l4 4" stroke="#999" stroke-width="2"/></svg>
</div>

<nav class="nav">
  <a class="active" href="#" style="left:592px;width:83px">HOME</a>
  <a href="#" style="left:695px;width:85px">CATEGORY</a>
  <a href="#" style="left:815px;width:85px">PRODUCT <svg width="8" height="5" viewBox="0 0 8 5" style="margin-left:4px;vertical-align:middle"><path d="M0 0h8L4 5z" fill="#555"/></svg></a>
  <a href="#" style="left:925px;width:80px">CONTACT</a>
  <a href="#" style="left:1035px;width:55px">BLOG</a>
</nav>

<div class="abs page"></div>
<div class="abs hero"></div>
<div class="abs hero-photo" role="img" aria-label="Person in a suit holding a touch panel tablet showing a dashboard"></div>
<h1 class="abs hero-title">Touch Panel PC/<br>Bedienterminal</h1>
<p class="abs hero-text">Lorem ipsum dolor sit amet, consectetur adipiicing elit, sed do eiusmod tempor incididunt.</p>
<div class="abs btn-start">GET STARTED</div>

<section class="abs features"></section>
<div class="abs features-top"></div>
<div class="abs divider" style="left:452px"></div>
<div class="abs divider" style="left:766px"></div>

<div class="abs product-img" style="left:215px;background:linear-gradient(135deg,#3c8a6a,#1f5a45 60%,#9a9a9a)" role="img" aria-label="Modbus interface card"></div>
<div class="abs product-img" style="left:530px;background:linear-gradient(135deg,#d0d0d0,#7a7a7a 55%,#2c2c2c)" role="img" aria-label="Handheld touch panel device"></div>
<div class="abs product-img" style="left:825px;background:linear-gradient(135deg,#3a3a3a,#111 60%,#b08a3a)" role="img" aria-label="Embedded system circuit board"></div>

<div class="abs band" style="left:128px;width:324px"></div>
<div class="abs band" style="left:453px;width:313px"></div>
<div class="abs band" style="left:767px;width:275px"></div>

<h2 class="abs feature-title" style="left:140px">MODBUS RTU</h2>
<h2 class="abs feature-title" style="left:456px">TOUCH PANEL</h2>
<h2 class="abs feature-title" style="left:754px">EMBEDDED SYSTEMS</h2>

<p class="abs feature-text" style="left:161px">Lorem ipsum dolor sit amet, consectetur adipisicing elit, sed do eiusmod tempor</p>
<p class="abs feature-text" style="left:477px;top:669px">Lorem ipsum dolor sit amet, consectetur adipisicing elit, sed do eiusmod tempor</p>
<p class="abs feature-text" style="left:788px;top:669px">Lorem ipsum dolor sit amet, consectetur adipisicing elit, sed do eiusmod tempor</p>

<div class="abs btn-learn" style="left:238px">LEARN MORE</div>
<div class="abs btn-learn" style="left:548px">LEARN MORE</div>
<div class="abs btn-learn" style="left:865px">LEARN MORE</div>

<footer>
  <div class="abs footer"></div>
  <h4 class="footer-heading" style="left:111px">SUPPORT</h4>
  <h4 class="footer-heading" style="left:373px">DIARY POSTS</h4>
  <h4 class="footer-heading" style="left:636px">DIARY TAGS</h4>
  <h4 class="footer-heading" style="left:881px">GALLERY</h4>

  <p class="abs support">For assistance or questions for our products, make sure you visit our support forums or call us at</p>
  <p class="abs support-phone">(555)804-3172</p>

  <div class="abs" style="left:373px;top:831px;width:225px">
    <div class="post-date">APRIL 6TH, 2013</div>
    <div class="post-title">It's time to tell our story right from the beginning</div>
    <div class="post-date" style="margin-top:16px">MARCH 27TH, 2013</div>
    <div class="post-title" style="width:240px">Take away the sorrow from my heart</div>
  </div>

  <div class="abs tags">
    <span class="tag">DREAMY</span><span class="tag">ETERNITY</span><span class="tag">MUSIC</span>
    <span class="tag">OTHER STORIES</span><span class="tag">POETRY</span>
    <span class="tag">UNIVERSE</span><span class="tag">WALL</span>
  </div>

  <div class="abs gallery">
    <div class="thumb"><span role="img" aria-label="Photo thumbnail" style="background:linear-gradient(135deg,#7fb6d8,#d8b44a)"></span></div>
    <div class="thumb"><span role="img" aria-label="Photo thumbnail" style="background:linear-gradient(135deg,#c0301a,#f0a030)"></span></div>
    <div class="thumb"><span role="img" aria-label="Photo thumbnail" style="background:linear-gradient(135deg,#f4d0d8,#e0a050)"></span></div>
    <div class="thumb"><span role="img" aria-label="Photo thumbnail" style="background:linear-gradient(135deg,#2a5ab0,#e06080)"></span></div>
    <div class="thumb"><span role="img" aria-label="Photo thumbnail" style="background:linear-gradient(135deg,#2c2c5a,#c07030)"></span></div>
    <div class="thumb"><span role="img" aria-label="Photo thumbnail" style="background:linear-gradient(135deg,#ffffff,#3aa040)"></span></div>
    <div class="thumb"><span role="img" aria-label="Photo thumbnail" style="background:linear-gradient(135deg,#3a4a9a,#d0a040)"></span></div>
    <div class="thumb"><span role="img" aria-label="Photo thumbnail" style="background:linear-gradient(135deg,#f0f0d0,#70c0a0)"></span></div>
  </div>

  <div class="abs legal">2013 © Velqora. ALL Rights Reserved. <span>Privacy Policy</span> | <span>Terms of Service</span></div>
</footer>

</body>
</html>
```